Book for a presidential campaign

We need a book front cover design for a presidential campaign. The title of the book is "Raise Every Harbor Higher!" Subtitle is "Notes From a Quiet Orchard" The candidate's name should be on the cover as well, so let's call him "Dorian Falke" so you have a name to use in your design. The candidate is nonpartisan, appealing to both liberals and conservatives. The solutions are out of the box and powerful, leading to the benefit of all.

```html
<!DOCTYPE html>
<html lang="en">
<head>
<meta charset="utf-8">
<title>Raise Every Harbor Higher! — Dorian Falke</title>
<link href="https://fonts.googleapis.com/css2?family=Luckiest+Guy&family=Open+Sans:ital,wght@0,700;1,400&display=swap" rel="stylesheet">
<style>
  :root {
    --paper: #ffffff;
    --gold: #eab30d;
    --gold-light: #f7d247;
    --gold-deep: #a97900;
    --ink-grey: #5a6268;
    --author-grey: #5f666b;
  }
  html, body {
    margin: 0;
    padding: 0;
    width: 847px;
    height: 1200px;
    overflow: hidden;
    background: var(--paper);
  }
  .cover {
    position: relative;
    width: 847px;
    height: 1200px;
    background: var(--paper);
  }
  .title {
    position: absolute;
    top: 82px;
    left: 0;
    width: 100%;
    margin: 0;
    text-align: center;
    font-family: "Luckiest Guy", "Impact", sans-serif;
    font-weight: 400;
    color: var(--gold);
    letter-spacing: 2px;
    text-shadow: 0 2px 0 var(--gold-light), 2px 4px 0 var(--gold-deep), 3px 6px 6px rgba(120, 80, 0, 0.35);
    line-height: 1.05;
  }
  .title-line { display: block; }
  .title-line--top { font-size: 100px; }
  .title-line--bottom { font-size: 78px; margin-top: 10px; }
  .growth-art {
    position: absolute;
    top: 360px;
    left: 0;
    width: 847px;
    height: 620px;
  }
  .subtitle-text {
    font-family: "Open Sans", Arial, sans-serif;
    font-weight: 700;
    font-size: 44px;
    fill: var(--ink-grey);
  }
  .author {
    position: absolute;
    top: 1052px;
    left: 0;
    width: 100%;
    margin: 0;
    text-align: center;
    font-family: "Open Sans", Arial, sans-serif;
    font-style: italic;
    font-weight: 400;
    font-size: 40px;
    color: var(--author-grey);
  }
</style>
</head>
<body>
  <main class="cover">
    <h1 class="title">
      <span class="title-line title-line--top">Raise Every</span>
      <span class="title-line title-line--bottom">Harbor Higher!</span>
    </h1>

    <svg class="growth-art" viewBox="0 360 847 620" xmlns="http://www.w3.org/2000/svg">
      <defs>
        <linearGradient id="coinTone" x1="0" y1="0" x2="0" y2="1">
          <stop offset="0" stop-color="#f3c94a"/>
          <stop offset="0.6" stop-color="#d9a22a"/>
          <stop offset="1" stop-color="#b9851c"/>
        </linearGradient>
        <linearGradient id="arrowTone" x1="0" y1="1" x2="1" y2="0">
          <stop offset="0" stop-color="#d7a032"/>
          <stop offset="1" stop-color="#f2c35a"/>
        </linearGradient>
        <path id="subtitleCurve" d="M 85 815 C 260 715 500 605 690 435"/>
      </defs>

      <path class="coin-stacks" role="img" aria-label="Rising stacks of gold coins, growing taller from left to right"
            fill="url(#coinTone)"
            d="M 88 945 L 88 878 L 210 878 L 210 840 L 340 840 L 340 772 L 470 772 L 470 702 L 582 702 L 582 620 L 690 620 L 690 540 L 800 540 L 800 900 Z"/>

      <g class="growth-arrow">
        <path d="M 78 862 C 300 790 560 690 760 400" fill="none" stroke="url(#arrowTone)" stroke-width="12" stroke-linecap="round"/>
        <polygon points="797,372 720,402 770,440" fill="#f0bd4f"/>
      </g>

      <text class="subtitle-text">
        <textPath href="#subtitleCurve">"Notes From a Quiet Orchard"</textPath>
      </text>
    </svg>

    <p class="author">Dorian Falke</p>
  </main>
</body>
</html>
```